Carpentry company Needs a business card design

We need a design for a Carpentry / building company, business card. Please think of designs out of the ordinary and try to make it eye catching. Our existing logo will need to be incorporated in the design. However feel free to change the colours of the logo to suit your design. I would like to see some designs with green /black and orange incorporated into it.These are not the only colours accepted and all designs that appeal will be accepted.

Please contact me should you have any questions
Thanks Martin

Target Market(s)

General Public seeking carpentry work

Industry/Entity Type

Business

Contact Information for Business Card

- Current company logo ( colours can be changed)
-Phone number ,
- info@brelvanbuild.com.au
- brelvanbuild.com.au
-the facebook symbol

Font styles to use
Other font styles liked:
• You choose

Requirements
Must have
• Services we provide
• - Renovations
• -Deckings & Pergolas
• -Kitchens
• - Bathrooms
• - Intricate details
Nice to have
• an awesome design
Should not have
• Tools on the business card

```html
<!DOCTYPE html>
<html lang="en">
<head>
<meta charset="utf-8">
<title>Brelvan Build – Business Card</title>
<link rel="stylesheet" href="https://fonts.googleapis.com/css2?family=Open+Sans:wght@400;600;700&display=swap">
<style>
  :root {
    --page: #d8d8d6;
    --card: #f5f5f3;
    --card-edge: #c9c9c6;
    --ink: #141414;
    --copper: #a8612a;
    --band-dark: #111111;
    --white: #ffffff;
  }
  * { box-sizing: border-box; margin: 0; padding: 0; }
  html, body {
    width: 1200px; height: 970px; overflow: hidden;
    background: var(--page);
    font-family: "Open Sans", sans-serif;
    color: var(--ink);
  }
  .card {
    position: absolute; left: 60px; top: 185px;
    width: 1080px; height: 600px;
    background: var(--card);
    border: 1px solid var(--card-edge);
    overflow: hidden;
  }
  .brand {
    position: absolute; left: 54px; top: 120px;
    display: flex; align-items: center; gap: 18px;
  }
  .brand-square { width: 34px; height: 34px; background: var(--copper); }
  .brand-name {
    font-size: 58px; font-weight: 700; letter-spacing: 2px;
    color: var(--ink); line-height: 1;
  }
  .services {
    position: absolute; right: 50px; top: 62px;
    list-style: none; text-align: right;
    font-size: 25px; line-height: 35.5px;
  }
  .services li { display: flex; justify-content: flex-end; align-items: center; gap: 10px; }
  .services svg { width: 24px; height: 24px; }
  .person {
    position: absolute; left: 54px; right: 50px; top: 342px;
    text-align: right;
  }
  .person-name { font-size: 32px; font-weight: 700; color: var(--copper); line-height: 44px; }
  .person-rule { height: 3px; background: var(--ink); margin: 4px 0 6px; }
  .person-role { font-size: 24px; line-height: 32px; }
  .contacts {
    position: absolute; left: 54px; top: 424px;
    list-style: none; font-size: 26px; line-height: 39px;
  }
  .contacts li { display: flex; align-items: center; gap: 12px; }
  .contacts svg { width: 26px; height: 26px; flex: none; }
  .bands { position: absolute; left: 0; bottom: 0; width: 1080px; height: 60px; }
  .website {
    position: absolute; right: 50px; bottom: 11px;
    font-size: 26px; letter-spacing: 2.5px; color: var(--white);
  }
</style>
</head>
<body>
  <div class="card">
    <div class="brand">
      <span class="brand-square"></span>
      <span class="brand-name">BRELVAN BUILD</span>
    </div>

    <ul class="services">
      <li>Renovations <svg viewBox="0 0 24 24"><rect x="3" y="3" width="18" height="18" rx="4" fill="#141414"/><path d="M12 6 L18 12 L12 18 L6 12Z" fill="#a8612a"/></svg></li>
      <li>Deckings &amp; Pergolas <svg viewBox="0 0 24 24"><rect x="3" y="3" width="18" height="18" rx="4" fill="#141414"/><path d="M12 6 L18 12 L12 18 L6 12Z" fill="#a8612a"/></svg></li>
      <li>Kitchens <svg viewBox="0 0 24 24"><rect x="3" y="3" width="18" height="18" rx="4" fill="#141414"/><path d="M12 6 L18 12 L12 18 L6 12Z" fill="#a8612a"/></svg></li>
      <li>Bathrooms <svg viewBox="0 0 24 24"><rect x="3" y="3" width="18" height="18" rx="4" fill="#141414"/><path d="M12 6 L18 12 L12 18 L6 12Z" fill="#a8612a"/></svg></li>
      <li>Intricate details <svg viewBox="0 0 24 24"><rect x="3" y="3" width="18" height="18" rx="4" fill="#141414"/><path d="M12 6 L18 12 L12 18 L6 12Z" fill="#a8612a"/></svg></li>
    </ul>

    <div class="person">
      <div class="person-name">Martin Calloway</div>
      <div class="person-rule"></div>
      <div class="person-role">Director</div>
    </div>

    <ul class="contacts">
      <li><svg viewBox="0 0 26 26" aria-label="Social page"><rect x="1" y="1" width="24" height="24" fill="#a8612a"/></svg>brelvanbuild</li>
      <li><svg viewBox="0 0 26 26" aria-label="Phone"><rect x="1" y="1" width="24" height="24" fill="#a8612a"/><path d="M6 9 Q13 4 20 9 L18 11 L16 9 L10 9 L8 11Z" fill="#f5f5f3"/><rect x="8" y="12" width="10" height="8" rx="1" fill="#f5f5f3"/></svg>000 000 0000</li>
      <li><svg viewBox="0 0 26 26" aria-label="Email"><rect x="1" y="1" width="24" height="24" fill="#a8612a"/><rect x="5" y="8" width="16" height="11" fill="none" stroke="#f5f5f3" stroke-width="1.6"/><path d="M5 8 L13 14 L21 8" fill="none" stroke="#f5f5f3" stroke-width="1.6"/></svg>info@brelvanbuild.com.au</li>
    </ul>

    <svg class="bands" viewBox="0 0 1080 60" preserveAspectRatio="none">
      <polygon points="0,35 620,35 608,60 0,60" fill="#a8612a"/>
      <polygon points="645,8 1080,8 1080,60 598,60" fill="#111111"/>
    </svg>
    <div class="website">brelvanbuild.com.au</div>
  </div>
</body>
</html>
```